Timber Ridge Land Services Business Cards

Need to create a business card with the company logo "Timber Ridge Land Services". The business will provide forestry mulching for land clearing and vegetation control, brush and small tree removal, wildlife habitat improvement and trail and property access creation.

```html
<!DOCTYPE html>
<html lang="en">
<head>
<meta charset="utf-8">
<title>Timber Ridge Land Services – Business Cards</title>
<link rel="stylesheet" href="https://fonts.googleapis.com/css2?family=Montserrat:wght@400;700&display=swap">
<style>
  :root {
    --backdrop: #ccd2d1;
    --paper: #f1f1ee;
    --forest: #0b4a33;
    --leaf: #5cc262;
    --ink: #2b2b2b;
    --white: #ffffff;
  }
  * { margin: 0; padding: 0; box-sizing: border-box; }
  html, body {
    width: 1200px; height: 881px; overflow: hidden;
    background: var(--backdrop);
    font-family: "Montserrat", Arial, sans-serif;
  }
  .sheet {
    position: relative; width: 1200px; height: 881px;
    display: flex; align-items: center; justify-content: center; gap: 60px;
  }
  .card {
    width: 510px; height: 292px;
    border-bottom: 5px solid var(--leaf);
    box-shadow: 0 14px 30px rgba(0,0,0,0.18);
    position: relative;
  }
  .card--front { background: var(--paper); }
  .card--back {
    background: var(--forest);
    display: flex; align-items: center; justify-content: center;
  }

  .front-layout {
    position: absolute; inset: 0;
    display: flex; align-items: center; justify-content: center; gap: 26px;
  }
  .identity { text-align: right; }
  .identity__name {
    color: var(--forest); font-weight: 700; font-size: 20px;
    letter-spacing: 0.3px; text-transform: uppercase;
  }
  .identity__role { color: var(--ink); font-size: 13px; margin-top: 4px; }
  .divider { width: 2px; height: 84px; background: var(--leaf); }
  .contacts { list-style: none; }
  .contacts__item {
    display: flex; align-items: center; gap: 8px;
    color: var(--ink); font-size: 13px; line-height: 1; margin: 7px 0;
  }
  .contacts__icon { width: 14px; height: 14px; flex: none; }

  .brand { display: flex; align-items: center; gap: 16px; }
  .brand__dot { width: 22px; height: 22px; border-radius: 50%; background: var(--white); flex: none; }
  .brand__name {
    color: var(--white); font-weight: 700; font-size: 30px;
    line-height: 1.15; text-transform: uppercase; letter-spacing: 1px;
  }
</style>
</head>
<body>
<main class="sheet">
  <section class="card card--front" aria-label="Card front">
    <div class="front-layout">
      <div class="identity">
        <p class="identity__name">Daniel Hayes</p>
        <p class="identity__role">Managing Director</p>
      </div>
      <div class="divider"></div>
      <ul class="contacts">
        <li class="contacts__item">
          <svg class="contacts__icon" viewBox="0 0 14 14"><circle cx="7" cy="7" r="7" fill="#5cc262"/><path d="M4.3 3.8l1.4-.3.7 1.7-.8.6a5 5 0 0 0 2.6 2.6l.6-.8 1.7.7-.3 1.4C7 10 4 7 4.3 3.8z" fill="#fff"/></svg>
          555 018 204
        </li>
        <li class="contacts__item">
          <svg class="contacts__icon" viewBox="0 0 14 14"><circle cx="7" cy="7" r="7" fill="#5cc262"/><rect x="3.5" y="4.5" width="7" height="5" fill="none" stroke="#fff" stroke-width="1"/><path d="M3.5 4.5L7 7.3l3.5-2.8" fill="none" stroke="#fff" stroke-width="1"/></svg>
          info@timberridgeland.com
        </li>
        <li class="contacts__item">
          <svg class="contacts__icon" viewBox="0 0 14 14"><circle cx="7" cy="7" r="7" fill="#5cc262"/><circle cx="7" cy="7" r="3.6" fill="none" stroke="#fff" stroke-width="0.9"/><path d="M3.4 7h7.2M7 3.4c-1.6 2-1.6 5.2 0 7.2M7 3.4c1.6 2 1.6 5.2 0 7.2" fill="none" stroke="#fff" stroke-width="0.8"/></svg>
          www.timberridgeland.com
        </li>
      </ul>
    </div>
  </section>

  <section class="card card--back" aria-label="Card back">
    <div class="brand">
      <span class="brand__dot"></span>
      <p class="brand__name">Timber Ridge<br>Land Services</p>
    </div>
  </section>
</main>
</body>
</html>
```